I need a professional modern flyer offering our crane services with our phone number and website. The flyer should focus on the blue crane and the red crane (JointArms) but include a small picture of the other cranes as well to show variety. This flyer will be mailed and emailed to a variety of roofing companies, HVAC, pool and mechanical contractors as well as precast concrete companies to attempt to earn their business. 8.5x11 single sided

HoistReadyRigging.example
555 814-2967 should be number on flyer

```html
<!DOCTYPE html>
<html lang="en">
<head>
<meta charset="utf-8">
<title>Hoist Ready Rigging – Crane Service Flyer</title>
<link rel="stylesheet" href="https://fonts.googleapis.com/css2?family=Saira+Condensed:wght@800;900&family=Poppins:wght@400;500;600;700&display=swap">
<style>
  :root{
    --red:#c01b2c;
    --red-bright:#e3202b;
    --green:#2ec444;
    --black:#1b1b1b;
    --white:#ffffff;
    --ink:#1e1e1e;
    --stage:#bdbdbd;
  }
  *{box-sizing:border-box;margin:0;padding:0}
  html,body{width:1200px;height:2400px;overflow:hidden}
  body{background:var(--stage);font-family:"Poppins",sans-serif;position:relative}
  .flyer{position:absolute;left:50px;top:489px;width:1100px;height:1422px;background:var(--white);overflow:hidden;box-shadow:0 10px 24px rgba(0,0,0,.25)}
  .hero-band{position:absolute;left:0;top:0;width:1100px;height:530px;background:var(--red)}
  .photo{position:absolute}
  .photo-boom-truck{left:640px;top:30px;width:460px;height:660px;background:linear-gradient(170deg,#2c3e8f 0%,#24357a 45%,#e9e9e9 70%,#6a6a6a 100%);border-radius:4px}
  .headline{position:absolute;left:70px;top:40px;font-family:"Saira Condensed",sans-serif;font-weight:900;font-style:italic;font-size:92px;line-height:78px;color:var(--white);letter-spacing:1px}
  .promise-bar{position:absolute;left:73px;top:223px;width:545px;height:54px;background:var(--black);color:var(--white);font-weight:700;font-size:36px;letter-spacing:5px;line-height:54px;padding-left:30px;white-space:nowrap}
  .tagline{position:absolute;left:76px;top:290px;width:700px;color:var(--white);font-size:22px;line-height:28px}
  .fleet-box{position:absolute;left:65px;top:372px;width:681px;height:157px;background:var(--green);color:var(--white);padding:14px 22px}
  .fleet-box h2{font-size:33px;font-weight:700;line-height:40px}
  .fleet-box p{font-size:21.5px;line-height:26px;margin-top:6px;padding-left:4px}
  .thumb{position:absolute;width:188px;height:167px;border:3px solid var(--green);border-radius:9px;padding:4px;background:var(--white)}
  .thumb span{display:block;width:100%;height:100%;border-radius:5px}
  .thumb-allterrain{left:58px;top:585px}
  .thumb-allterrain span{background:linear-gradient(160deg,#f2b51c,#d08d0a 60%,#3b3b3b)}
  .thumb-cab{left:259px;top:585px}
  .thumb-cab span{background:linear-gradient(160deg,#2a2a2a,#dcdcdc 50%,#1a1a1a)}
  .thumb-forklift{left:259px;top:762px;z-index:2}
  .thumb-forklift span{background:linear-gradient(160deg,#ffffff,#f1f1f1 40%,#d63a2c 65%,#3a3a3a)}
  .photo-jointarm{left:0;top:779px;width:480px;height:418px;background:linear-gradient(170deg,#f3f3f3 0%,#c9c9c9 40%,#d5452e 60%,#2b2b2b 100%)}
  .fleet-list{position:absolute;left:499px;top:697px;width:545px;display:grid;grid-template-columns:1fr 1fr;}
  .fleet-item{display:flex;align-items:center;gap:26px;height:80px;font-weight:500;font-size:22px;line-height:25px;color:var(--ink);padding-left:6px}
  .fleet-item:nth-child(odd){border-right:1px dashed var(--green)}
  .fleet-item:nth-child(even){padding-left:40px}
  .fleet-item:nth-child(-n+2){border-bottom:1px dashed var(--green)}
  .fleet-item svg{flex:none}
  .services-bar{position:absolute;left:495px;top:886px;width:274px;height:46px;background:var(--black);color:var(--green);font-weight:700;font-size:31px;line-height:46px;padding-left:10px;white-space:nowrap}
  .service{position:absolute;display:flex;align-items:center;gap:10px;font-size:17.5px;line-height:20px;color:var(--ink)}
  .service svg{flex:none}
  .contact-bar{position:absolute;left:696px;top:1170px;width:404px;height:46px;background:var(--red-bright);color:var(--white);font-weight:700;font-size:35px;letter-spacing:5px;line-height:46px;padding-left:26px;z-index:2;white-space:nowrap}
  .footer{position:absolute;left:0;top:1197px;width:1100px;height:225px;background:var(--black)}
  .brand{position:absolute;left:95px;top:95px;display:flex;align-items:center;gap:12px;color:var(--white);font-weight:700;font-size:26px;white-space:nowrap}
  .brand i{width:18px;height:18px;background:var(--green);display:block}
  .office{position:absolute;top:36px;color:var(--white);font-size:16.5px;line-height:20px;white-space:nowrap}
  .office b{font-weight:700}
  .office .pin{position:absolute;left:-18px;top:3px}
  .office .phone{display:flex;align-items:center;gap:6px;font-weight:700;font-size:20px;margin-top:22px;margin-left:-18px}
  .office-oh{left:492px}
  .office-in{left:789px}
  .visit-bar{position:absolute;left:452px;top:142px;width:612px;height:38px;background:var(--green);color:var(--white);display:flex;align-items:center;padding-left:14px;white-space:nowrap;overflow:hidden}
  .visit-bar small{flex:none;font-size:16px;letter-spacing:2.5px;width:112px;line-height:38px}
  .visit-bar strong{flex:none;font-size:21px;letter-spacing:1.5px;font-weight:700;line-height:38px}
</style>
</head>
<body>
<main class="flyer">
  <div class="hero-band"></div>
  <div class="photo photo-boom-truck" role="img" aria-label="Blue truck-mounted crane with white cab lifting a load"></div>

  <h1 class="headline">CRANE<br>SERVICE</h1>
  <div class="promise-bar">DONE AS PROMISED</div>
  <p class="tagline">Crane service partners that meet deadlines, prioritize safety, and stay within budget with end-to-end support.</p>

  <section class="fleet-box">
    <h2>OUR CRANE FLEET</h2>
    <p>We’ll help you choose the right crane<br>based on your project specs, terrain,<br>and lifting requirements. View our fleet.</p>
  </section>

  <div class="photo photo-jointarm" role="img" aria-label="Red jointed-arm crane on a truck beside a building"></div>
  <div class="thumb thumb-allterrain"><span role="img" aria-label="Yellow all-terrain crane"></span></div>
  <div class="thumb thumb-cab"><span role="img" aria-label="White crane truck cab"></span></div>
  <div class="thumb thumb-forklift"><span role="img" aria-label="Red rough-terrain forklift"></span></div>

  <div class="fleet-list">
    <div class="fleet-item">
      <svg width="60" height="44" viewBox="0 0 60 44"><path d="M6 30h40v6H6z M10 22h14v8H10z" fill="#222"/><path d="M18 22L44 4l4 4" stroke="#d8202b" stroke-width="4" fill="none"/><line x1="48" y1="8" x2="48" y2="20" stroke="#222" stroke-width="2"/><circle cx="14" cy="38" r="5" fill="#222"/><circle cx="38" cy="38" r="5" fill="#222"/></svg>
      <span>All-Terrain<br>Cranes</span>
    </div>
    <div class="fleet-item">
      <svg width="50" height="50" viewBox="0 0 50 50"><path d="M4 34h40v6H4z M26 22h12v12H26z" fill="#222"/><path d="M14 34V20l14-12 6 6" stroke="#d8202b" stroke-width="4" fill="none"/><circle cx="12" cy="44" r="5" fill="#222"/><circle cx="36" cy="44" r="5" fill="#222"/></svg>
      <span>JointArms</span>
    </div>
    <div class="fleet-item">
      <svg width="60" height="56" viewBox="0 0 60 56"><path d="M6 38h46v8H6z M38 28h14v10H38z" fill="#222"/><path d="M14 38L26 6l6 4" stroke="#d8202b" stroke-width="4" fill="none"/><line x1="32" y1="10" x2="32" y2="24" stroke="#222" stroke-width="2"/><circle cx="14" cy="49" r="5" fill="#222"/><circle cx="44" cy="49" r="5" fill="#222"/></svg>
      <span>Truck Cranes</span>
    </div>
    <div class="fleet-item">
      <svg width="50" height="40" viewBox="0 0 50 40"><path d="M4 6v28h10" stroke="#222" stroke-width="3" fill="none"/><path d="M14 14h14v16H14z" fill="#d8202b"/><rect x="32" y="10" width="12" height="16" fill="none" stroke="#d8202b" stroke-width="2"/><circle cx="18" cy="34" r="5" fill="#222"/><circle cx="30" cy="34" r="4" fill="#222"/></svg>
      <span>Forklift</span>
    </div>
  </div>

  <div class="services-bar">OUR SERVICES</div>

  <div class="service" style="left:494px;top:993px">
    <svg width="58" height="58" viewBox="0 0 58 58"><circle cx="29" cy="29" r="27" fill="#fff" stroke="#2ec444" stroke-width="3"/><circle cx="29" cy="29" r="22" fill="#d8202b"/><path d="M32 16l-10 15h7l-3 12 10-16h-7z" fill="none" stroke="#fff" stroke-width="2"/></svg>
    <span>Power<br>Transformer</span>
  </div>
  <div class="service" style="left:694px;top:993px">
    <svg width="58" height="58" viewBox="0 0 58 58"><circle cx="29" cy="29" r="27" fill="#fff" stroke="#2ec444" stroke-width="3"/><circle cx="29" cy="29" r="22" fill="#d8202b"/><path d="M20 42V18h18v24 M20 26h18 M20 34h18 M29 18v24" fill="none" stroke="#fff" stroke-width="2"/></svg>
    <span>Steel<br>Construction</span>
  </div>
  <div class="service" style="left:893px;top:993px">
    <svg width="58" height="58" viewBox="0 0 58 58"><circle cx="29" cy="29" r="27" fill="#fff" stroke="#2ec444" stroke-width="3"/><circle cx="29" cy="29" r="22" fill="#d8202b"/><path d="M17 24h24v14H17z M22 24v14 M29 24v14 M36 24v14 M23 24l6-6 6 6" fill="none" stroke="#fff" stroke-width="2"/></svg>
    <span>Container</span>
  </div>
  <div class="service" style="left:494px;top:1066px">
    <svg width="58" height="58" viewBox="0 0 58 58"><circle cx="29" cy="29" r="27" fill="#fff" stroke="#2ec444" stroke-width="3"/><circle cx="29" cy="29" r="22" fill="#d8202b"/><path d="M22 42V16 M14 20h28 M22 16l-6 4 M38 20v8 M18 42h10" fill="none" stroke="#fff" stroke-width="2"/></svg>
    <span>General<br>Construction</span>
  </div>
  <div class="service" style="left:694px;top:1066px">
    <svg width="58" height="58" viewBox="0 0 58 58"><circle cx="29" cy="29" r="27" fill="#fff" stroke="#2ec444" stroke-width="3"/><circle cx="29" cy="29" r="22" fill="#d8202b"/><path d="M16 38h16v-8h-8z M32 30l8-12 4 4 M40 18v10" fill="none" stroke="#fff" stroke-width="2"/><circle cx="20" cy="40" r="2" fill="#fff"/><circle cx="28" cy="40" r="2" fill="#fff"/></svg>
    <span>Heavy<br>Machinery<br>Moving</span>
  </div>
  <div class="service" style="left:893px;top:1066px">
    <svg width="58" height="58" viewBox="0 0 58 58"><circle cx="29" cy="29" r="27" fill="#fff" stroke="#2ec444" stroke-width="3"/><circle cx="29" cy="29" r="22" fill="#d8202b"/><path d="M17 26h24v12H17z M22 32h6 M34 32h2 M24 26v-6h10v6" fill="none" stroke="#fff" stroke-width="2"/></svg>
    <span>HVAC</span>
  </div>
  <div class="service" style="left:494px;top:1136px">
    <svg width="58" height="58" viewBox="0 0 58 58"><circle cx="29" cy="29" r="27" fill="#fff" stroke="#2ec444" stroke-width="3"/><circle cx="29" cy="29" r="22" fill="#d8202b"/><path d="M16 38h18v-8h-6z M34 30l6-12 4 2 M20 22a5 5 0 1 1 8 0" fill="none" stroke="#fff" stroke-width="2"/></svg>
    <span>Tree/<br>Landscape</span>
  </div>

  <div class="contact-bar">GET IN TOUCH</div>

  <footer class="footer">
    <div class="brand"><i></i>Hoist Ready Rigging</div>

    <div class="office office-oh">
      <svg class="pin" width="12" height="16" viewBox="0 0 12 16"><path d="M6 0a6 6 0 0 1 6 6c0 4-6 10-6 10S0 10 0 6a6 6 0 0 1 6-6z" fill="#2ec444"/><circle cx="6" cy="6" r="2.2" fill="#1b1b1b"/></svg>
      <b>OHIO</b><br>1180 Harlow Ave, Akron,<br>OH 44300
      <div class="phone"><svg width="14" height="14" viewBox="0 0 14 14"><circle cx="7" cy="7" r="7" fill="#2ec444"/><path d="M4.5 3.5l1.5 1.7-.8 1a5 5 0 0 0 2.6 2.6l1-.8 1.7 1.5-.9 1.1c-3 0-6.2-3.2-6.2-6.2z" fill="#fff"/></svg>555 814-2967</div>
    </div>

    <div class="office office-in">
      <svg class="pin" width="12" height="16" viewBox="0 0 12 16"><path d="M6 0a6 6 0 0 1 6 6c0 4-6 10-6 10S0 10 0 6a6 6 0 0 1 6-6z" fill="#2ec444"/><circle cx="6" cy="6" r="2.2" fill="#1b1b1b"/></svg>
      <b>INDIANA</b><br>4820 Meadow Ln, Noblesville,<br>IN 46000
      <div class="phone"><svg width="14" height="14" viewBox="0 0 14 14"><circle cx="7" cy="7" r="7" fill="#2ec444"/><path d="M4.5 3.5l1.5 1.7-.8 1a5 5 0 0 0 2.6 2.6l1-.8 1.7 1.5-.9 1.1c-3 0-6.2-3.2-6.2-6.2z" fill="#fff"/></svg>555 814-2967</div>
    </div>

    <div class="visit-bar"><small>VISIT AT</small><strong>www.HoistReadyRigging.example</strong></div>
  </footer>
</main>
</body>
</html>
```